Business Card Design Project

I need a business card designed that is clean, simple and elegant.
I am a fashion and advertising photographer based in Cape Town and Durban South Africa.
check out my website: www.marlowvance.co.za for ideas
Updates
Hi all,
Thanks for your submissions so far!
Please note:
I want no more than than black, white and/or grey to be used.
I don't want any photos used.
I would like the card to be double sided.
I would like to continue the design similar to the past ones Ive used.
I hope this helps, please send me further questions should you have any.
many thanks!
Marlow
Hi,
Please have a look at the jpg I loaded(called inspiration) which is the direction or inspiration I am aiming at.
Also PLEASE remember NO PHOTOS to be included on the card
many thanks!!
Target Market(s)
You can look at my site to get a better understanding of the audience:
www.marlowvance.co.za
Industry/Entity Type
Advertising
Requirements
Must have
- Clean design which can also be used for a watermark on photographs
perhaps black background with white text/grey
company called: Marlow Vance Photography
Nice to have
- below I have added logos that I have used in the past.
Should not have
- pictures of cameras
tacky elements

```html
<!DOCTYPE html>
<html lang="en">
<head>
<meta charset="utf-8">
<title>Marlow Vance Photography – Business Card</title>
<link rel="stylesheet" href="https://fonts.googleapis.com/css2?family=Archivo+Narrow:wght@400;700&family=Roboto+Condensed:wght@400;700&display=swap">
<style>
  :root {
    --backdrop: #9ea6a6;
    --card: #e6e9e9;
    --circle: #e8ebeb;
    --ink: #4a4d4f;
    --ink-soft: #6b6f72;
    --label: #ffffff;
    --shadow: #1c1c1c;
  }
  html, body {
    margin: 0;
    padding: 0;
    overflow: hidden;
    background: var(--backdrop);
  }
  .canvas {
    display: block;
    width: 1200px;
    height: 576px;
  }
  .brand-name {
    font-family: "Archivo Narrow", "Arial Narrow", sans-serif;
    font-weight: 700;
    font-size: 24px;
    letter-spacing: 0.5px;
  }
  .back-name {
    font-family: "Archivo Narrow", "Arial Narrow", sans-serif;
    font-weight: 700;
    font-size: 21px;
    letter-spacing: 1.5px;
    fill: var(--ink-soft);
  }
  .contact-line {
    font-family: "Roboto Condensed", Arial, sans-serif;
    font-size: 13px;
    fill: var(--ink-soft);
  }
  .state-label {
    font-family: "Roboto Condensed", Arial, sans-serif;
    font-weight: 700;
    font-size: 33px;
    letter-spacing: 2px;
    fill: var(--label);
  }
  .spec-text {
    font-family: "Roboto Condensed", Arial, sans-serif;
    font-size: 19px;
    letter-spacing: 0.6px;
    fill: #333638;
  }
</style>
</head>
<body>
<svg class="canvas" viewBox="0 0 1200 576" xmlns="http://www.w3.org/2000/svg">
  <defs>
    <linearGradient id="metal-ink" x1="0" y1="0" x2="0" y2="1">
      <stop offset="0" stop-color="#8a8e90"/>
      <stop offset="0.55" stop-color="#3e4143"/>
      <stop offset="1" stop-color="#6a6e70"/>
    </linearGradient>
    <filter id="soft-shadow" x="-20%" y="-20%" width="140%" height="140%">
      <feGaussianBlur stdDeviation="9"/>
    </filter>
    <clipPath id="front-clip"><rect x="57" y="72" width="510" height="288"/></clipPath>
    <clipPath id="back-clip"><rect x="621" y="72" width="510" height="288"/></clipPath>
  </defs>

  <rect class="backdrop" width="1200" height="576" fill="var(--backdrop)"/>

  <g class="card-front">
    <rect x="57" y="72" width="510" height="288" fill="var(--card)"/>
    <g clip-path="url(#front-clip)">
      <circle cx="433" cy="219" r="143" fill="var(--shadow)" opacity="0.85" filter="url(#soft-shadow)"/>
      <circle cx="423" cy="219" r="145" fill="var(--circle)"/>
    </g>
    <text class="brand-name" x="87" y="229" textLength="171" lengthAdjust="spacingAndGlyphs" fill="url(#metal-ink)">MARLOW VANCE</text>
    <text class="brand-name" x="280" y="229" textLength="170" lengthAdjust="spacingAndGlyphs" fill="url(#metal-ink)">PHOTOGRAPHY</text>
  </g>

  <g class="card-back">
    <rect x="621" y="72" width="510" height="288" fill="var(--card)"/>
    <g clip-path="url(#back-clip)">
      <circle cx="712" cy="219" r="143" fill="var(--shadow)" opacity="0.85" filter="url(#soft-shadow)"/>
      <circle cx="722" cy="219" r="145" fill="var(--circle)"/>
    </g>
    <text class="back-name" x="925" y="170" textLength="180" lengthAdjust="spacingAndGlyphs">MARLOW VANCE</text>

    <g class="phone-icon" fill="var(--ink-soft)">
      <path d="M931 213 q18 -10 37 0 l0 5 l-8 2 l-2 -3 q-9 -2 -18 0 l-2 3 l-7 -2 z"/>
      <path d="M937 222 h25 l5 13 h-35 z"/>
      <circle cx="949.5" cy="228.5" r="3.5" fill="var(--card)"/>
    </g>
    <text class="contact-line" x="976" y="220">+27 (0)82 555 0147</text>
    <text class="contact-line" x="976" y="235">+27 (0)31 555 0193</text>

    <text class="contact-line" x="920" y="279" textLength="187" lengthAdjust="spacingAndGlyphs">WWW.MARLOWVANCE.CO.ZA</text>
  </g>

  <text class="state-label" x="57" y="449" textLength="123" lengthAdjust="spacingAndGlyphs">CLOSED</text>
  <text class="state-label" x="1008" y="449" textLength="124" lengthAdjust="spacingAndGlyphs">OPENED</text>

  <g class="spec-bar">
    <rect x="57" y="494" width="1073" height="49" fill="var(--card)"/>
    <text class="spec-text" x="142" y="527" textLength="870" lengthAdjust="spacingAndGlyphs" xml:space="preserve">CMYK COLOR  #e1e1e1   SIZE :1063 x 591   CIRCLE SIZE: W 616px  H: 597 px</text>
  </g>
</svg>
</body>
</html>
```